Design Template for use with our Career Cluster Maps

***Update 11/24*** - Please see K7M Future Set Model (attached) for color scheme and targeted look and feel. Also, focus on content displayed in the Construction Cluster document (attached). All information displayed in the Construction Cluster document needs to be included in the design. Need a clean, simple design. Unique ideas for organizing content are welcomed.

We need a unique design for our curriculum maps. I have two copies that are models, both are good but are not unique to us as a company. We provide the data that allows the templates to be filled in by clients, so don't worry about the actual data, just what can we design around how the data is displayed. Our main website is ladderforwork.example , feel free to use anything from that site as well as the colors. I am attaching the 2 designs as well as some unique pictures that can be incorporated. The design when final will go into our software platform and the data will be pulled and placed for schools to use automatically, again looking for a design that captures the idea between the job market and job preparedness. I have added an additional document that shows "all the pathways" and how our software pulls the data and puts on a template. The template we desire needs to be updated, the two additional files show how our clients have tried to update the template with a better look and feel. We want a better look and feel in our platform.
Updates

Please post the design as a PDF but we need the In-Design files so that we can edit and use within our system

```html
<!DOCTYPE html>
<html lang="en">
<head>
<meta charset="utf-8">
<title>Ladder For Work Career Cluster Map – Architecture &amp; Construction</title>
<link href="https://fonts.googleapis.com/css2?family=Oswald:wght@400;500&family=Roboto+Condensed:wght@400;700&display=swap" rel="stylesheet">
<style>
:root{
  --stage:#a9abae;
  --paper:#ffffff;
  --band:#e7e7e8;
  --ink:#2f2f2f;
  --dark:#4d4d4f;
  --orange:#f28c28;
  --yellow:#f6bf4b;
  --teal:#3f9fb1;
  --blue:#5e9bd6;
  --zone1:#535355;
  --t-gray:#ececec;
  --t-yellow:#fdf2dd;
  --t-teal:#e2eff2;
  --t-orange:#fdece1;
  --t-blue:#e3eef8;
}
*{box-sizing:border-box;margin:0;padding:0}
html,body{width:1200px;height:2315px;overflow:hidden;background:var(--stage)}
body{font-family:"Roboto Condensed",Arial,sans-serif;color:var(--ink)}
.board{position:absolute;left:0;top:0;width:1335px;height:2576px;transform:scale(.8989);transform-origin:0 0}
.page{position:absolute;left:123px;width:1099px;height:777px;background:var(--paper);overflow:hidden}
.abs{position:absolute}
/* brand: plain name with one circle */
.brand{position:absolute;display:flex;align-items:center;gap:8px;font-family:"Oswald",sans-serif;font-weight:500;font-size:22px;line-height:1;color:var(--orange);white-space:nowrap}
.brand .dot{width:14px;height:14px;border-radius:50%;background:var(--orange);flex:none}
/* page 1 */
.band{position:absolute;left:4px;right:0;background:var(--band)}
.side-bar{position:absolute;left:77px;top:152px;width:73px;height:625px;background:var(--dark)}
.side-bar .label{position:absolute;left:50%;top:50%;transform:translate(-50%,-50%) rotate(-90deg);white-space:nowrap;font-family:"Oswald",sans-serif;font-size:30px;color:#fff}
.side-bar .tick{position:absolute;left:32px;width:8px;height:50px;background:#8d8d8f}
.cluster{position:absolute;width:190px}
.cluster .icon{width:30px;height:30px;display:block;margin-bottom:6px}
.cluster h3{font-size:10.5px;line-height:14px;font-weight:400;color:var(--orange);margin-bottom:6px}
.cluster ul{list-style:none}
.cluster li{font-size:8.8px;line-height:12.6px;padding-left:16px;position:relative;white-space:nowrap}
.cluster li::before{content:"";position:absolute;left:0;top:3px;width:6px;height:6px;background:var(--orange)}
.photo-wash{position:absolute;background:linear-gradient(90deg,rgba(255,255,255,0),rgba(200,205,212,.35));}
/* header banners */
.hero{position:absolute;left:0;top:0;width:1099px;height:200px;background:linear-gradient(180deg,#c9ced4 0%,#dfe3e7 55%,rgba(255,255,255,0) 100%)}
.title-box{position:absolute;left:289px;width:522px;height:88px;background:rgba(78,78,80,.88);color:#fff;font-family:"Oswald",sans-serif;font-size:33px;display:flex;align-items:center;justify-content:center;letter-spacing:.3px}
.subhead{position:absolute;left:77px;font-family:"Oswald",sans-serif;font-size:20px;color:var(--ink)}
/* job zones */
.zone{position:absolute;top:210px;width:188px;height:452px}
.zone-head{height:72px;color:#fff;padding:14px 0 0 28px}
.zone-head b{display:block;font-family:"Oswald",sans-serif;font-weight:400;font-size:24px;line-height:28px}
.zone-head span{font-size:9px}
.zone-body{height:380px;padding:10px 0 0 28px}
.job{position:relative;height:76px;font-size:10px;line-height:13px}
.job .t{color:var(--dark)}
.job .row{display:flex;color:var(--orange);font-size:9px;line-height:12.5px;width:132px}
.job .row i{flex:1;border-bottom:1px dotted var(--orange);margin:0 2px 4px;font-style:normal}
.star{position:absolute;right:6px;top:0;width:16px;height:16px;border-radius:50%;background:var(--orange);color:var(--dark);font-size:11px;line-height:16px;text-align:center}
.zone-note{color:var(--orange);font-size:10px;text-align:center;padding:14px 12px 0 0;line-height:13px}
.legend{position:absolute;left:77px;font-size:8.8px;line-height:12px}
.legend .hl{color:var(--orange)}
.legend .big{font-family:"Oswald",sans-serif;font-size:16px;color:var(--orange)}
.foot-r{position:absolute;font-size:8.6px}
.badge{display:inline-block;width:12px;height:12px;border-radius:50%;background:var(--blue);vertical-align:middle;margin:0 3px 0 8px}
.badge-name{color:var(--blue);font-size:13px;vertical-align:middle}
/* page 3 grid */
.req{position:absolute;left:77px;top:195px;display:grid;grid-template-columns:repeat(8,117.6px);grid-template-rows:45px repeat(4,33.5px)}
.req .h{color:#fff;font-size:12.5px;font-weight:700;display:flex;align-items:center;justify-content:center;text-align:center;line-height:14px}
.req .c{font-size:8.8px;display:flex;align-items:center;justify-content:center;text-align:center;line-height:11px;border-right:1px solid #fff}
.req .alt{background:#eeeeef}
.req .merge{grid-row:2 / 6;grid-column:8;background:var(--t-blue);font-size:8.8px;text-align:center;padding:14px 6px;line-height:11px}
.block-head{position:absolute;color:#fff;font-size:12px;font-weight:700;display:flex;align-items:center;justify-content:center;text-align:center;line-height:14px}
.block-body{position:absolute;font-size:8.8px;line-height:12px}
.sq{display:inline-block;width:6px;height:6px;margin-right:10px;vertical-align:1px}
.line{display:inline-block;width:70px;border-bottom:1px solid var(--ink);margin-left:6px}
.ribbon{position:absolute;left:222px;width:145px;height:31px;color:#fff;font-size:11.5px;font-weight:700;display:flex;align-items:center;padding-left:28px;clip-path:polygon(0 0,88% 0,100% 50%,88% 100%,0 100%)}
.deg{position:absolute;font-size:8.8px;text-align:center;display:flex;align-items:center;justify-content:center;line-height:11px;border-right:1px solid #fff;height:31px}
</style>
</head>
<body>
<div class="board">

<!-- PAGE 1: cluster overview -->
<section class="page" style="top:41px">
  <div class="band" style="top:222px;height:158px"></div>
  <div class="band" style="top:544px;height:198px"></div>
  <div class="photo-wash" style="left:252px;top:30px;width:840px;height:190px" role="img" aria-label="Faint background photographs of people at work for each career cluster"></div>

  <div class="brand" style="left:45px;top:70px"><span class="dot"></span>Ladder For Work</div>

  <div class="side-bar">
    <div class="tick" style="top:38px"></div>
    <div class="label">Career Clusters and Pathways</div>
    <div class="tick" style="top:532px"></div>
  </div>

  <!-- row 1 -->
  <div class="cluster" style="left:252px;top:48px">
    <svg class="icon" viewBox="0 0 30 30"><path d="M15 4v24M9 10l6 5 6-5M9 16l6 5 6-5" stroke="#4d4d4f" stroke-width="2.4" fill="none"/></svg>
    <h3>Agriculture, Food &amp;<br>Natural Resources</h3>
    <ul><li>Agribusiness Systems</li><li>Animal Systems</li><li>Environmental Service Systems</li><li>Food Products &amp; Processing Systems</li><li>Natural Resources Systems</li><li>Plant Systems</li><li>Power, Structural &amp; Technical Systems</li></ul>
  </div>
  <div class="cluster" style="left:455px;top:48px">
    <svg class="icon" viewBox="0 0 30 30"><path d="M4 11h22L15 4z" fill="#f28c28"/><path d="M7 13v11M12 13v11M18 13v11M23 13v11M4 26h22" stroke="#4d4d4f" stroke-width="2.4"/></svg>
    <h3>Government &amp; Public<br>Administration</h3>
    <ul><li>Foreign Service</li><li>Governance</li><li>National Security</li><li>Planning</li><li>Public Management &amp; Administration</li><li>Regulation</li><li>Revenue &amp; Taxation</li></ul>
  </div>
  <div class="cluster" style="left:645px;top:48px">
    <svg class="icon" viewBox="0 0 30 30"><path d="M15 4v22M6 8h18M10 26h10M6 8l-4 9h8zM24 8l-4 9h8z" stroke="#4d4d4f" stroke-width="2" fill="none"/></svg>
    <h3>Law, Public Safety,<br>Corrections &amp; Security</h3>
    <ul><li>Correction Services</li><li>Emergency &amp; Fire Management Services</li><li>Law Enforcement Services</li><li>Legal Services</li><li>Security &amp; Protective Services</li></ul>
  </div>
  <div class="cluster" style="left:841px;top:55px">
    <svg class="icon" viewBox="0 0 30 30"><path d="M15 26C4 18 3 12 6 8s8-3 9 1c1-4 6-5 9-1s2 10-9 18z" fill="#f28c28" stroke="#4d4d4f" stroke-width="2"/><path d="M15 11v8M11 15h8" stroke="#fff" stroke-width="2.4"/></svg>
    <h3>Health Science</h3>
    <ul><li>Biotechnology Research &amp; Development</li><li>Diagnostic Services</li><li>Health Informatics</li><li>Support Services</li><li>Therapeutic Services</li></ul>
  </div>

  <!-- row 2 -->
  <div class="cluster" style="left:252px;top:235px">
    <svg class="icon" viewBox="0 0 30 30"><path d="M4 11h6l12-6v20l-12-6H4z" fill="#f28c28" stroke="#4d4d4f" stroke-width="2"/><path d="M8 19l2 7" stroke="#4d4d4f" stroke-width="2.4"/></svg>
    <h3>Marketing</h3>
    <ul><li>Marketing Communications</li><li>Marketing Management</li><li>Marketing Research</li><li>Merchandising</li><li>Professional Sales</li></ul>
  </div>
  <div class="cluster" style="left:455px;top:228px">
    <svg class="icon" viewBox="0 0 30 30"><path d="M15 4a11 11 0 1 0 0 22c3 0 3-3 1-4s0-4 3-4h5A11 11 0 0 0 15 4z" fill="#f28c28" stroke="#4d4d4f" stroke-width="2"/><circle cx="10" cy="12" r="2" fill="#4d4d4f"/><circle cx="16" cy="9" r="2" fill="#4d4d4f"/></svg>
    <h3>Arts, A/V Technology &amp;<br>Communications</h3>
    <ul><li>A/V Technology &amp; Film</li><li>Journalism &amp; Broadcasting</li><li>Performing Arts</li><li>Printing Technology</li><li>Telecommunications</li><li>Visual Arts</li></ul>
  </div>
  <div class="cluster" style="left:645px;top:235px">
    <svg class="icon" viewBox="0 0 30 30"><rect x="4" y="8" width="22" height="18" rx="3" fill="#f28c28" stroke="#4d4d4f" stroke-width="2"/><path d="M11 8V5h8v3" stroke="#4d4d4f" stroke-width="2" fill="none"/><circle cx="15" cy="16" r="3" fill="#4d4d4f"/></svg>
    <h3>Hospitality &amp; Tourism</h3>
    <ul><li>Lodging</li><li>Recreation, Amusements &amp; Attractions</li><li>Restaurants &amp; Food/Beverage Services</li><li>Travel &amp; Tours</li></ul>
  </div>
  <div class="cluster" style="left:841px;top:235px">
    <svg class="icon" viewBox="0 0 30 30"><circle cx="12" cy="16" r="7" fill="none" stroke="#4d4d4f" stroke-width="3" stroke-dasharray="3 2"/><circle cx="22" cy="8" r="4" fill="none" stroke="#f28c28" stroke-width="2.4"/></svg>
    <h3>Manufacturing</h3>
    <ul><li>Health, Safety &amp; Environmental Assurance</li><li>Logistics &amp; Inventory Control</li><li>Maintenance, Installation &amp; Repair</li><li>Manufacturing Production Process Development</li><li>Production</li><li>Quality Assurance</li></ul>
  </div>

  <!-- row 3 -->
  <div class="cluster" style="left:252px;top:392px">
    <svg class="icon" viewBox="0 0 30 30"><rect x="4" y="4" width="22" height="17" fill="none" stroke="#4d4d4f" stroke-width="2"/><path d="M9 18v-4M13 18v-7M17 18v-5M21 18v-9" stroke="#f28c28" stroke-width="2.4"/><path d="M15 21l-5 7M15 21l5 7" stroke="#4d4d4f" stroke-width="2"/></svg>
    <h3>Business, Management<br>&amp; Administration</h3>
    <ul><li>Administrative Support</li><li>Business Information Management</li><li>General Management</li><li>Human Resources Management</li><li>Operations Management</li></ul>
  </div>
  <div class="cluster" style="left:455px;top:392px">
    <svg class="icon" viewBox="0 0 30 30"><g fill="none" stroke="#4d4d4f" stroke-width="1.8"><ellipse cx="15" cy="15" rx="12" ry="4.5"/><ellipse cx="15" cy="15" rx="12" ry="4.5" transform="rotate(60 15 15)"/><ellipse cx="15" cy="15" rx="12" ry="4.5" transform="rotate(120 15 15)"/></g><circle cx="15" cy="15" r="2.6" fill="#f28c28"/></svg>
    <h3>Science, Technology,<br>Engineering &amp; Mathematics</h3>
    <ul><li>Engineering &amp; Technology</li><li>Science &amp; Mathematics</li></ul>
  </div>
  <div class="cluster" style="left:645px;top:392px">
    <svg class="icon" viewBox="0 0 30 30"><path d="M6 28V18a9 9 0 1 1 14 6v4z" fill="#f28c28"/><rect x="16" y="2" width="12" height="9" rx="2" fill="#4d4d4f"/></svg>
    <h3>Human Services</h3>
    <ul><li>Consumer Services</li><li>Counseling &amp; Mental Health Services</li><li>Early Childhood Development &amp; Services</li><li>Family &amp; Community Services</li><li>Personal Care Services</li></ul>
  </div>
  <div class="cluster" style="left:841px;top:392px">
    <svg class="icon" viewBox="0 0 30 30"><path d="M2 9l13-6 13 6-13 6z" fill="#f28c28"/><path d="M8 12v6c4 3 10 3 14 0v-6" fill="#4d4d4f"/><rect x="5" y="22" width="20" height="5" fill="#4d4d4f"/></svg>
    <h3>Education &amp; Training</h3>
    <ul><li>Administration &amp; Administrative Support</li><li>Professional Support Services</li><li>Teaching/Training</li></ul>
  </div>

  <!-- row 4 -->
  <div class="cluster" style="left:252px;top:548px">
    <svg class="icon" viewBox="0 0 30 30"><rect x="2" y="2" width="8" height="8" fill="#f28c28"/><rect x="12" y="10" width="8" height="8" fill="#4d4d4f"/><rect x="20" y="18" width="8" height="8" fill="#f28c28"/><path d="M6 10v12h14M16 18v8" stroke="#4d4d4f" stroke-width="2" fill="none"/></svg>
    <h3>Information Technology</h3>
    <ul><li>Information Support &amp; Services</li><li>Network Systems</li><li>Programming &amp; Software Development</li><li>Web &amp; Digital Communications</li></ul>
  </div>
  <div class="cluster" style="left:455px;top:548px">
    <svg class="icon" viewBox="0 0 30 30"><path d="M5 26v-8h5v8zM12 26V13h5v13zM19 26V8h5v18z" fill="#4d4d4f"/><path d="M4 16l8-8 5 4 9-9" stroke="#f28c28" stroke-width="2.4" fill="none"/></svg>
    <h3>Finance</h3>
    <ul><li>Accounting</li><li>Banking Services</li><li>Business Finance</li><li>Insurance</li><li>Securities &amp; Investments</li></ul>
  </div>
  <div class="cluster" style="left:645px;top:548px">
    <svg class="icon" viewBox="0 0 30 30"><path d="M6 28V12h18v16z" fill="none" stroke="#4d4d4f" stroke-width="2"/><path d="M15 2v10" stroke="#4d4d4f" stroke-width="2"/><rect x="11" y="16" width="8" height="8" fill="#f28c28"/></svg>
    <h3>Architecture &amp;<br>Construction</h3>
    <ul><li>Construction</li><li>Design/Pre-Construction</li><li>Maintenance/Operations</li></ul>
  </div>
  <div class="cluster" style="left:841px;top:548px;width:230px">
    <svg class="icon" viewBox="0 0 40 30" style="width:40px"><rect x="2" y="8" width="22" height="14" fill="#f28c28"/><path d="M24 12h8l6 6v4H24z" fill="#4d4d4f"/><circle cx="9" cy="24" r="3" fill="#4d4d4f"/><circle cx="31" cy="24" r="3" fill="#4d4d4f"/></svg>
    <h3>Transportation,<br>Distribution &amp; Logistics</h3>
    <ul><li>Facility &amp; Mobile Equipment Maintenance</li><li>Health, Safety &amp; Environmental Management</li><li>Logistics Planning &amp; Management Services</li><li>Sales &amp; Service</li><li>Transportation Operations</li><li>Transportation Systems/Infrastructure Planning,<br>Management &amp; Regulation</li><li>Warehousing &amp; Distribution Center Operations</li></ul>
  </div>
</section>

<!-- PAGE 2: regional career opportunities -->
<section class="page" style="top:875px">
  <div class="hero" role="img" aria-label="Photo of a hand placing a model house on a table"></div>
  <div class="brand" style="left:82px;top:90px"><span class="dot"></span>Ladder For Work</div>
  <div class="title-box" style="top:57px">ARCHITECTURE &amp; CONSTRUCTION</div>
  <div class="subhead" style="top:170px">Regional Career Opportunities – Listed by Highest Projected Demand</div>

  <div class="zone" style="left:77px">
    <div class="zone-head" style="background:var(--zone1)"><b>JOB ZONE 01</b><span>High School Diploma or Less</span></div>
    <div class="zone-body" style="background:var(--t-gray)">
      <div class="job"><div class="t">Landscaping and<br>Groundskeeping Workers</div><div class="row">Annual Openings =<i></i>825</div><div class="row">Median Wage =<i></i>$27,810</div></div>
      <div class="job"><span class="star">★</span><div class="t">Roustabouts, Oil and Gas</div><div class="row">Annual Openings =<i></i>678</div><div class="row">Median Wage =<i></i>$34,810</div></div>
      <div class="job"><span class="star">★</span><div class="t">Derrick Operators, Oil and Gas</div><div class="row">Annual Openings =<i></i>214</div><div class="row">Median Wage =<i></i>$48,010</div></div>
      <div class="job"><span class="star">★</span><div class="t">Cement Masons and Concrete<br>Finishers</div><div class="row">Annual Openings =<i></i>150</div><div class="row">Median Wage =<i></i>$37,660</div></div>
      <div class="job"><span class="star">★</span><div class="t">Plasterers and Stucco Masons</div><div class="row">Annual Openings =<i></i>57</div><div class="row">Median Wage =<i></i>$38,720</div></div>
    </div>
  </div>
  <div class="zone" style="left:266px">
    <div class="zone-head" style="background:var(--yellow)"><b>JOB ZONE 02</b><span>High School Diploma</span></div>
    <div class="zone-body" style="background:var(--t-yellow)">
      <div class="job"><div class="t">Construction Laborers</div><div class="row">Annual Openings =<i></i>1690</div><div class="row">Median Wage =<i></i>$31,980</div></div>
      <div class="job"><span class="star">★</span><div class="t">Carpenters</div><div class="row">Annual Openings =<i></i>648</div><div class="row">Median Wage =<i></i>$38,430</div></div>
      <div class="job"><span class="star">★</span><div class="t">Operating Engineers and Other<br>Construction Equi...</div><div class="row">Annual Openings =<i></i>575</div><div class="row">Median Wage =<i></i>$43,300</div></div>
      <div class="job"><span class="star">★</span><div class="t">Service Unit Operators, Oil,<br>Gas, and Mining</div><div class="row">Annual Openings =<i></i>271</div><div class="row">Median Wage =<i></i>$64,470</div></div>
      <div class="job"><div class="t">Roofers</div><div class="row">Annual Openings =<i></i>212</div><div class="row">Median Wage =<i></i>$33,360</div></div>
    </div>
  </div>
  <div class="zone" style="left:454px">
    <div class="zone-head" style="background:var(--teal)"><b>JOB ZONE 03</b><span>Certificate or Associate's Degree</span></div>
    <div class="zone-body" style="background:var(--t-teal)">
      <div class="job"><span class="star">★</span><div class="t">First-Line Supervisors of<br>Construction Trades a...</div><div class="row">Annual Openings =<i></i>876</div><div class="row">Median Wage =<i></i>$58,730</div></div>
      <div class="job"><span class="star">★</span><div class="t">Electricians</div><div class="row">Annual Openings =<i></i>611</div><div class="row">Median Wage =<i></i>$49,040</div></div>
      <div class="job"><span class="star">★</span><div class="t">Plumbers, Pipefitters,<br>and Steamfitters</div><div class="row">Annual Openings =<i></i>373</div><div class="row">Median Wage =<i></i>$44,260</div></div>
      <div class="job"><span class="star">★</span><div class="t">First-Line Supervisors of<br>Landscaping, Lawn Ser...</div><div class="row">Annual Openings =<i></i>160</div><div class="row">Median Wage =<i></i>$47,550</div></div>
      <div class="job"><span class="star">★</span><div class="t">Heating, Air Conditioning, and<br>Refrigeration Me...</div><div class="row">Annual Openings =<i></i>153</div><div class="row">Median Wage =<i></i>$43,450</div></div>
    </div>
  </div>
  <div class="zone" style="left:642px">
    <div class="zone-head" style="background:var(--orange)"><b>JOB ZONE 04</b><span>Bachelor's Degree</span></div>
    <div class="zone-body" style="background:var(--t-orange)">
      <div class="job"><span class="star">★</span><div class="t">Construction Managers</div><div class="row">Annual Openings =<i></i>221</div><div class="row">Median Wage =<i></i>$87,060</div></div>
      <div class="job"><span class="star">★</span><div class="t">Civil Engineers</div><div class="row">Annual Openings =<i></i>128</div><div class="row">Median Wage =<i></i>$86,590</div></div>
      <div class="job"><span class="star">★</span><div class="t">Cost Estimators</div><div class="row">Annual Openings =<i></i>115</div><div class="row">Median Wage =<i></i>$57,410</div></div>
      <div class="job"><span class="star">★</span><div class="t">Architectural and Civil<br>Drafters</div><div class="row">Annual Openings =<i></i>81</div><div class="row">Median Wage =<i></i>$50,910</div></div>
      <div class="job"><span class="star">★</span><div class="t">Architects, Except<br>Landscape and Naval</div><div class="row">Annual Openings =<i></i>50</div><div class="row">Median Wage =<i></i>$72,460</div></div>
    </div>
  </div>
  <div class="zone" style="left:830px">
    <div class="zone-head" style="background:var(--blue)"><b>JOB ZONE 05</b><span>Master's or Doctorate Degree</span></div>
    <div class="zone-body" style="background:var(--t-blue)">
      <p class="zone-note">Few regional occupations in this pathway require education at this degree level.</p>
    </div>
  </div>

  <div class="legend" style="top:690px">
    <span class="star" style="position:absolute;left:0;top:0;width:14px;height:14px;line-height:14px;font-size:9px">★</span>
    <p style="padding-left:30px">Top five high-value occupations in this pathway for the <span class="hl">Northern Middle Tennessee Region</span></p>
    <p style="padding-left:30px;margin-top:8px">Occupations with the highest annual openings that are stable or growing with median wages above <span class="big">$35,000</span> are considered high-value.</p>
    <p style="padding-left:30px;margin-top:2px"><span class="hl" style="position:absolute;left:2px;font-size:16px">*</span>State level data was used due to limitations in regional data.</p>
  </div>
  <div class="foot-r" style="left:777px;top:712px">Explore careers at <span style="color:var(--blue)">regiondata.example</span><span class="badge"></span><span class="badge-name">RDA</span></div>
  <div class="foot-r" style="left:777px;top:740px">Northstar Ed Ladder For Work 2018 Trademark Northstar Ed, LLC</div>
</section>

<!-- PAGE 3: high school requirements and programs -->
<section class="page" style="top:1722px">
  <div class="hero" role="img" aria-label="Photo of construction workers in safety vests on a building site" style="height:210px;background:linear-gradient(180deg,#b9b6ad 0%,#d7d4cc 60%,rgba(255,255,255,0) 100%)"></div>
  <div class="brand" style="left:105px;top:73px"><span class="dot"></span>Ladder For Work</div>
  <div class="title-box" style="top:40px;height:84px">ARCHITECTURE &amp; CONSTRUCTION</div>
  <div class="subhead" style="left:73px;top:160px">Regional High School Requirements and Programs (Grades 9-12)</div>

  <div class="req">
    <div class="h" style="background:var(--yellow)">English<br>Language Arts</div>
    <div class="h" style="background:var(--teal)">Math</div>
    <div class="h" style="background:var(--orange)">Science</div>
    <div class="h" style="background:var(--blue)">Social Studies</div>
    <div class="h" style="background:var(--yellow)">Foreign<br>Language</div>
    <div class="h" style="background:var(--teal)">Physical<br>Education</div>
    <div class="h" style="background:var(--orange)">Fine Arts</div>
    <div class="h" style="background:var(--blue)">Elective Focus</div>

    <div class="c">English I</div><div class="c">Integrated I</div><div class="c">Biology</div><div class="c">World History and<br>Geography</div><div class="c">Foreign Language I</div><div class="c">Lifetime Wellness</div><div class="c">Fine Arts Selection</div>
    <div class="merge">Minimum of Three<br>Courses<br><i>See career programs<br>and electives below.</i><br><br><br><i>One Additional<br>Elective is Required</i></div>
    <div class="c alt">English II</div><div class="c alt">Integrated II</div><div class="c alt">Chemistry</div><div class="c alt">U.S. History and<br>Geography</div><div class="c alt">Foreign Language II</div><div class="c alt">Physical Education<br>(.5)</div><div class="c alt">------</div>
    <div class="c">English III</div><div class="c">Integrated III</div><div class="c">Physics</div><div class="c">Economics /<br>Government</div><div class="c">------</div><div class="c">------</div><div class="c">------</div>
    <div class="c alt">English IV</div><div class="c alt">Upper Level Math</div><div class="c alt">------</div><div class="c alt">Personal Finance<br>(.5)</div><div class="c alt">------</div><div class="c alt">------</div><div class="c alt">------</div>
  </div>

  <!-- program blocks -->
  <div class="block-head" style="left:77px;top:392px;width:145px;height:38px;background:var(--yellow)">Career Programs</div>
  <div class="block-body" style="left:77px;top:430px;width:145px;height:140px;background:var(--t-yellow);padding:40px 0 0 14px">
    <p><span class="sq" style="background:var(--yellow)"></span>Supply Chain Management</p>
    <p style="margin-top:30px;font-style:italic;padding-right:4px">*Note: Programs and courses may vary by high school.</p>
  </div>
  <div class="block-head" style="left:222px;top:392px;width:211px;height:38px;background:var(--teal)">Career Program Courses<br>and Related Courses</div>
  <div class="block-body" style="left:222px;top:430px;width:211px;height:140px;background:var(--t-teal);padding:18px 0 0 28px;line-height:18.5px">
    <p><span class="sq" style="background:var(--teal)"></span>Career Exploration</p>
    <p><span class="sq" style="background:var(--teal)"></span>Foundations of Transportation,</p>
    <p style="padding-left:16px">Distribution, &amp; Logistics</p>
    <p><span class="sq" style="background:var(--teal)"></span>Supply Chain Management I</p>
    <p><span class="sq" style="background:var(--teal)"></span>Supply Chain Management II</p>
    <p><span class="sq" style="background:var(--teal)"></span>Work-Based Learning / Practicum</p>
  </div>
  <div class="block-head" style="left:433px;top:392px;width:222px;height:38px;background:var(--blue)">Additional Electives</div>
  <div class="block-body" style="left:433px;top:430px;width:222px;height:140px;background:var(--t-blue);padding:18px 0 0 14px;display:grid;grid-template-columns:116px 100px;line-height:16px">
    <div>English Language Arts<br><span class="sq" style="background:var(--blue)"></span><br><span class="sq" style="background:var(--blue)"></span><span class="line"></span><br><br>Math<br><span class="sq" style="background:var(--blue)"></span><span class="line"></span><br><span class="sq" style="background:var(--blue)"></span><span class="line"></span></div>
    <div>Science<br><span class="sq" style="background:var(--blue)"></span><span class="line"></span><br><span class="sq" style="background:var(--blue)"></span><span class="line"></span><br><br>Other<br><span class="sq" style="background:var(--blue)"></span><span class="line"></span><br><span class="sq" style="background:var(--blue)"></span><span class="line"></span></div>
  </div>
  <div class="block-head" style="left:665px;top:392px;width:353px;height:38px;background:var(--orange)">Regional Postsecondary Schools</div>
  <div class="block-head" style="left:665px;top:430px;width:176px;height:38px;background:var(--teal)">Certificates and<br>Associate's Degrees</div>
  <div class="block-head" style="left:842px;top:430px;width:176px;height:38px;background:var(--blue)">Bachelor's and<br>Advanced Degrees</div>
  <div class="block-body" style="left:665px;top:468px;width:176px;height:102px;background:var(--t-teal);padding:20px 0 0 14px;line-height:11.5px">
    <p style="font-weight:700">Community Colleges</p>
    <p><span class="sq" style="background:var(--teal);margin-right:6px"></span>Harlow Valley Community College</p>
    <p><span class="sq" style="background:var(--teal);margin-right:6px"></span>Ridgeview College of</p>
    <p style="padding-left:12px">Applied Technology</p>
    <p><span class="sq" style="background:var(--teal);margin-right:6px"></span>Riverbend State Community College</p>
  </div>
  <div class="block-body" style="left:842px;top:468px;width:176px;height:102px;background:var(--t-blue);padding:20px 0 0 14px;line-height:11.5px">
    <p style="font-weight:700">Colleges and Universities</p>
    <p><span class="sq" style="background:var(--blue);margin-right:6px"></span>Central Plains State University</p>
    <p><span class="sq" style="background:var(--blue);margin-right:6px"></span>Oakmont State University</p>
    <p><span class="sq" style="background:var(--blue);margin-right:6px"></span>University of Eastbrook</p>
    <p><span class="sq" style="background:var(--blue);margin-right:6px"></span>Whitfield University</p>
  </div>

  <!-- postsecondary programs -->
  <div class="abs" style="left:85px;top:584px;font-family:'Oswald',sans-serif;font-size:18px;line-height:24px;color:var(--orange)">Postsecondary<br>Programs/Majors<br>for Occupations<br>in this Pathway</div>
  <div class="abs" style="left:367px;top:584px;width:651px;height:31px;background:var(--t-yellow)"></div>
  <div class="abs" style="left:367px;top:615px;width:651px;height:31px;background:var(--t-teal)"></div>
  <div class="abs" style="left:367px;top:646px;width:651px;height:31px;background:var(--t-blue)"></div>
  <div class="ribbon" style="top:584px;background:var(--yellow)">Certificate or A</div>
  <div class="ribbon" style="top:615px;background:var(--teal)">Bachelor's Degree</div>
  <div class="ribbon" style="top:646px;background:var(--blue)">Advanced Degree</div>

  <div class="deg" style="left:367px;top:584px;width:120px">Parts, Warehousing, and<br>Inventory Management</div>
  <div class="deg" style="left:487px;top:584px;width:133px">Business Administration and<br>Management</div>
  <div class="deg" style="left:620px;top:584px;width:134px">General Office and Clerical<br>Services</div>
  <div class="deg" style="left:754px;top:584px;width:131px">***</div>
  <div class="deg" style="left:885px;top:584px;width:133px">***</div>

  <div class="deg" style="left:367px;top:615px;width:120px">Business Administration<br>and Management</div>
  <div class="deg" style="left:487px;top:615px;width:133px">Logistics, Materials, and<br>Supply Chain Management</div>
  <div class="deg" style="left:620px;top:615px;width:134px">Consumer Merchandising/<br>Retailing Management</div>
  <div class="deg" style="left:754px;top:615px;width:131px">Transportation/Mobility<br>Management</div>
  <div class="deg" style="left:885px;top:615px;width:133px">Operations Management<br>and Supervision</div>

  <div class="deg" style="left:367px;top:646px;width:120px">***</div>
  <div class="deg" style="left:487px;top:646px;width:133px">***</div>
  <div class="deg" style="left:620px;top:646px;width:134px">***</div>
  <div class="deg" style="left:754px;top:646px;width:131px">***</div>
  <div class="deg" style="left:885px;top:646px;width:133px">***</div>

  <div class="abs" style="left:77px;top:697px;width:941px;border-top:1.5px solid var(--dark)"></div>
  <div class="abs" style="left:83px;top:708px;font-size:8.6px">*** Few regional occupations in this pathway require education at this degree level.</div>
  <div class="abs" style="left:783px;top:711px;font-size:8.6px">Northstar Ed Ladder For Work 2018 Trademark Northstar Ed, LLC</div>
</section>

</div>
</body>
</html>
```